Research project presentation flyer

Pending approval of a cooperative research project we need a flyer to present and "market" the academic project to the businesses we want to invite to participate.

The project is a cooperation between three different universities and businesses in the Nordic/Baltic countries and the subject is innovation and entrepreneurship (see the attached "raw" edition).

The intended audience will be all those directly involved with the project, media, municipalities/government, businesses and also the public.

The flyer needs to be in multiple language-editions, but the design must of course be identical. For this designproject, we submit the English content (please correct the English in the attached proposal as necessary). Thus the project result must be in a format that allows us to replace the English text with other languages ourselves.

The proposal attached is just that: a laymans proposal (and the content). Please feel free to rearrange content (and redesign!)

The format of the flyer is a folded A4 (i.e. A5 portrait), with print on both sides.

The raw edition that is attached contains a map that is merely a suggestion (low quality). A better map - perhaps with less irrelevant detail - must be proposed. The important part of the map is to show the location of the universities and project office.

Also, the "logo" of the project is of low quality, and must be changed. A core concept of the project is "triple helix", so the "logo" of the project should be something to that effect (triple helix), as indicated. The "logo" is only an illustration to be used on the flyer. The aim is not to develop a logo for the project. We will do that at a later stage.

The flyer is supposed to be downloadable from a project web, both in hi-res for printing in a professional printshop, and for printing on an average office colour printer. Designs that bleeds off the paper-edge might therefore be a challenge, as office-printers don't print to the edge of the paper.

Reason: Due to Easter holiday and few submissons.

Printing

• Format: A4 folded once, i.e. A5 portrait
Must be able to alter text in design to produce flyers in other languages that English (i.e. pdf is good for the English version, but editable fileformat must also be submitted)
Map must be improved
Logo must be improved. Concept: triple helix
• Clean, professional design.
Flyer is "selling" an academic project that must appeal to businesses

```html
<!DOCTYPE html>
<html lang="en">
<head>
<meta charset="utf-8">
<title>InnoNord Project Activities – Flyer Spread</title>
<link rel="stylesheet" href="https://fonts.googleapis.com/css2?family=Comfortaa:wght@400;500&family=Lato:wght@400;700&display=swap">
<style>
  :root {
    --backdrop: #e9eaec;
    --page-left: #f8f9fb;
    --fold-shade: #c6c7c9;
    --page-right: #f4f4f5;
    --sand: #f0d98e;
    --rule: #e8cf86;
    --sky: #1aa3e0;
    --ink: #5d5f63;
    --ink-strong: #4a4c50;
    --white: #ffffff;
    --bulb-light: #e4e4e6;
    --bulb-glow: #f2d489;
    --partner-red: #b2283a;
    --partner-blue: #1b7fc0;
    --partner-navy: #1d5f97;
  }
  * { box-sizing: border-box; margin: 0; padding: 0; }
  html, body {
    width: 1200px; height: 900px; overflow: hidden;
    background: var(--backdrop);
  }
  .spread {
    position: absolute; left: 62px; top: 71px;
    width: 1076px; height: 758px;
    font-family: "Lato", Arial, sans-serif;
    color: var(--ink);
    box-shadow: 0 6px 24px rgba(0,0,0,0.15);
  }
  .page-left {
    position: absolute; left: 0; top: 0; width: 539px; height: 100%;
    background: var(--page-left);
  }
  .page-right {
    position: absolute; left: 539px; top: 0; width: 537px; height: 100%;
    background: linear-gradient(90deg, var(--fold-shade) 0%, #e2e2e3 18%, var(--page-right) 40%);
    overflow: hidden;
  }
  .bulb-photo {
    position: absolute; left: 150px; top: 0; width: 387px; height: 100%;
    background:
      radial-gradient(ellipse 150px 130px at 330px 360px, var(--bulb-glow) 0%, rgba(242,212,137,0.4) 45%, rgba(242,212,137,0) 100%),
      linear-gradient(90deg, rgba(228,228,230,0) 0%, var(--bulb-light) 35%, #ececed 100%);
  }
  .intro-banner {
    position: absolute; left: 52px; top: 45px; width: 409px; height: 125px;
    background: var(--sand); border-radius: 14px;
    padding: 36px 18px 0 20px;
    color: var(--white); font-weight: 700; font-size: 14px; line-height: 18.5px;
  }
  .title {
    position: absolute; left: 57px; top: 190px;
    font-family: "Comfortaa", "Trebuchet MS", sans-serif; font-weight: 500;
    font-size: 34px; color: var(--sky); white-space: nowrap;
  }
  .language {
    position: absolute; left: 57px; top: 250px;
    font-size: 16px; font-weight: 700; color: #77797d;
  }
  .rule { position: absolute; height: 2px; background: var(--rule); }
  .rule-left { left: 57px; top: 287px; width: 400px; }
  .rule-right { left: 48px; top: 287px; width: 244px; }
  .wp-intro {
    position: absolute; left: 58px; top: 311px; width: 401px;
    font-size: 14px; font-weight: 700; line-height: 19px;
    color: var(--ink-strong); text-align: justify;
  }
  .wp {
    position: absolute; font-size: 14px; line-height: 18.5px;
    padding-left: 46px; text-indent: -46px;
  }
  .wp-label { color: var(--sky); font-weight: 700; }
  .wp-01 { left: 58px; top: 366px; width: 400px; }
  .wp-02 { left: 60px; top: 421px; width: 400px; }
  .wp-03 { left: 58px; top: 458px; width: 402px; }
  .wp-04 { left: 48px; top: 366px; width: 240px; }
  .wp-05 { left: 48px; top: 550px; width: 240px; }
  .partner-strip {
    position: absolute; left: 60px; top: 640px; width: 785px; height: 96px;
    background: var(--white); border-radius: 12px;
  }
  .partner {
    position: absolute; top: 50%; transform: translateY(-50%);
    font-family: "Lato", Arial, sans-serif; font-weight: 700; font-size: 20px;
    white-space: nowrap; display: flex; align-items: center; gap: 8px;
  }
  .partner-programme { left: 34px; color: #4b4d52; }
  .partner-university { left: 262px; color: var(--partner-red); font-size: 18px; }
  .partner-agency { left: 520px; color: var(--partner-blue); }
  .partner-college { left: 630px; color: var(--partner-navy); font-size: 16px; }
  .partner-college .dot {
    width: 64px; height: 64px; border-radius: 50%;
    background: var(--partner-navy); flex: none;
  }
</style>
</head>
<body>
  <main class="spread">
    <section class="page-left">
      <div class="intro-banner">
        Application to the NORDLINK program: NORDLINK Horizontal, through “Northern Agency for Study Exchange, NASE”
      </div>
      <h1 class="title">InnoNord Project Activities</h1>
      <p class="language">Project language: English</p>
      <div class="rule rule-left"></div>
      <p class="wp-intro">The project tasks will be subdivided into the following WorkPackages – WPs</p>
      <p class="wp wp-01"><span class="wp-label">WP 01:</span> Project administration, process- and economic control, information and reporting.</p>
      <p class="wp wp-02"><span class="wp-label">WP 02:</span> Development and support of the project web-portal</p>
      <p class="wp wp-03"><span class="wp-label">WP 03:</span>Analysis and development of the concept “Innovation and Entrepreneurship” (IE) within the partner institutions and the work practice within the involved innovation centres. Cooperation with trade/industry and governmental organisations through innovation centres or corresponding organisations for channeling contact with work life. Development of differentiated courses within IE – and testing of these.</p>
    </section>

    <section class="page-right">
      <div class="bulb-photo" role="img" aria-label="Photograph of a pile of white light bulbs with one bulb glowing warm yellow"></div>
      <div class="rule rule-right"></div>
      <p class="wp wp-04"><span class="wp-label">WP 04:</span>Dissemination of project results and experiences. Producing printed material on project results and experiences, presentation of results at international conferences. Concluding international conference on IE in Fjellby early summer 2014.</p>
      <p class="wp wp-05"><span class="wp-label">WP 05:</span> Evaluation</p>
    </section>

    <footer class="partner-strip">
      <span class="partner partner-programme">NORDLINK Horizontal</span>
      <span class="partner partner-university">Lindholm University</span>
      <span class="partner partner-agency">NASE</span>
      <span class="partner partner-college"><span class="dot"></span>Fjordvik College</span>
    </footer>
  </main>
</body>
</html>
```